Industrial Project Sign

We need an eye catching (but professional) industrial project sign that will be very large (roughly 12' high x 18' wide). This sign will be highly visible from the adjacent high speed highway.

* The following needs to be at the bottom of the signage: Logo (uploaded), Name (Pillar Ventures Group, Inc.) (uploaded) and phone number (555)613-8874

*Name of Project - "Brambleford Industrial Center"

* Text items
Land for Sale
Build to Suit
Zoning: Industrial (G I & L I)

* Interesting background that is eye catching
Updates

Good morning all,

We are considering all designers options as we go and are waiting for the final designs to come in by the 4th so that we can give each one a good look.   If you have any new designs, questions, further design options or any tweeks you want to do to current designs, please do so at this time.

Thanks to all of you for your submissions.

Industry/Entity Type

Industrial

```html
<!DOCTYPE html>
<html lang="en">
<head>
<meta charset="utf-8">
<title>Brambleford Industrial Center – Project Sign</title>
<link rel="stylesheet" href="https://fonts.googleapis.com/css2?family=Righteous&family=Tinos:wght@700&display=swap">
<style>
  :root {
    --sky: #27a8e1;
    --cyan: #42c5f2;
    --navy: #33317a;
    --magenta: #d9118b;
    --mist: #eef1f9;
    --white: #ffffff;
    --ink: #2b2b2b;
    --grey: #555555;
  }
  html, body { margin: 0; padding: 0; overflow: hidden; background: var(--white); }
  .sign {
    position: relative;
    width: 1200px;
    height: 803px;
    overflow: hidden;
    background: var(--white);
    font-family: "Righteous", sans-serif;
  }
  .backdrop { position: absolute; inset: 0; }
  .backdrop .field-sky { fill: var(--sky); }
  .backdrop .field-cyan { fill: var(--cyan); }
  .backdrop .field-navy { fill: var(--navy); }
  .backdrop .field-magenta { fill: var(--magenta); }
  .backdrop .field-mist { fill: var(--mist); }

  .brand-corner {
    position: absolute;
    left: 1010px;
    top: 210px;
    width: 176px;
    text-align: center;
    font-family: "Tinos", serif;
    font-weight: 700;
    font-size: 38px;
    color: var(--white);
    letter-spacing: 1px;
  }

  .launch {
    position: absolute;
    left: 44px;
    top: 212px;
    margin: 0;
    font-family: "Tinos", serif;
    font-weight: 700;
    font-size: 72px;
    line-height: 1;
    color: var(--white);
  }
  .project-name {
    position: absolute;
    left: 42px;
    top: 308px;
    margin: 0;
    font-weight: 400;
    font-size: 64px;
    line-height: 70px;
    letter-spacing: 2px;
    color: var(--navy);
    text-transform: uppercase;
  }
  .offer-list {
    position: absolute;
    left: 42px;
    top: 476px;
    margin: 0;
    padding: 0;
    list-style: none;
    color: var(--white);
    font-size: 36px;
    line-height: 49px;
    letter-spacing: 1.5px;
    text-transform: uppercase;
  }
  .offer-list li { display: flex; align-items: center; }
  .offer-list .diamond { width: 18px; height: 26px; margin-right: 14px; flex: none; }

  .company {
    position: absolute;
    left: 686px;
    top: 656px;
    width: 320px;
    display: flex;
    align-items: center;
  }
  .company .mark { width: 56px; height: 56px; background: var(--ink); flex: none; margin-right: 14px; }
  .company .details { flex: 1; }
  .company .name {
    font-family: "Tinos", serif;
    font-weight: 700;
    font-size: 16px;
    color: var(--grey);
    padding-bottom: 3px;
    border-bottom: 2px solid var(--ink);
  }
  .company .web {
    font-family: "Tinos", serif;
    font-size: 13px;
    color: var(--grey);
    padding-top: 4px;
  }

  .enquiries {
    position: absolute;
    left: 600px;
    top: 734px;
    width: 480px;
    margin: 0;
    text-align: center;
    color: var(--navy);
    font-size: 23px;
    line-height: 28px;
    letter-spacing: 1px;
    text-transform: uppercase;
  }
</style>
</head>
<body>
<main class="sign">
  <svg class="backdrop" width="1200" height="803" viewBox="0 0 1200 803" aria-hidden="true">
    <polygon class="field-mist" points="955,170 1200,490 1200,803 1090,803 805,408"/>
    <polygon class="field-sky" points="0,0 490,0 805,408 560,803 0,803"/>
    <polygon class="field-cyan" points="490,0 822,0 955,170 805,408"/>
    <polygon class="field-navy" points="822,0 1060,0 955,170"/>
    <polygon class="field-magenta" points="1060,0 1200,0 1200,490 955,170"/>
  </svg>

  <div class="brand-corner">PILLAR</div>

  <p class="launch">Launching</p>
  <h1 class="project-name">Brambleford<br>Industrial Center</h1>

  <ul class="offer-list">
    <li><svg class="diamond" viewBox="0 0 18 26"><polygon points="9,3 15,13 9,23 3,13" fill="none" stroke="#fff" stroke-width="3"/></svg>Land for Sale</li>
    <li><svg class="diamond" viewBox="0 0 18 26"><polygon points="9,3 15,13 9,23 3,13" fill="none" stroke="#fff" stroke-width="3"/></svg>Build to Suit</li>
    <li><svg class="diamond" viewBox="0 0 18 26"><polygon points="9,3 15,13 9,23 3,13" fill="none" stroke="#fff" stroke-width="3"/></svg>Zoning: Industrial (G I &amp; L I)</li>
  </ul>

  <div class="company">
    <div class="mark"></div>
    <div class="details">
      <div class="name">Pillar Ventures Group, Inc.</div>
      <div class="web">www.pillarventuresgroup.com</div>
    </div>
  </div>

  <p class="enquiries">For enquiries,<br>please contact us at (555)613-8874</p>
</main>
</body>
</html>
```